New home maintenance business, on the back of business card i would like dot points of my services provided.
these include,
General household repairs and maintenance
Painting
Verolin/Plaster Repairs
Fencing
Gardening and landscaping
Cleaning and removals
Doors and windows
Hinges and Locks
Fly screen/ screen door Repairs
I like black,silver, red but ill leav it up to you guys as something may be better for business.. , would also it be possible to create a logo for me incorporating the K&T as i want to make up t shirts in future thankyou
i would also like to put Marco Vintelli on the cards aswell please, and on back change painter to proffesional painter and decorator, please
i like alot of the designs sofar, i cant put my finger on wat 1 yet though!! cheers guys
Business
K&T HOME MAINTENANCE SERVICES
Lewis Vintelli 0467205184
kntmaintenance@postvale.com
ABN:57140328619

```html
<!DOCTYPE html>
<html lang="en">
<head>
<meta charset="utf-8">
<title>K&amp;T Home Maintenance Services – Business Card</title>
<link href="https://fonts.googleapis.com/css2?family=Source+Sans+3:wght@400&display=swap" rel="stylesheet">
<style>
  :root {
    --stage: #a8aaad;
    --card: #000000;
    --ink: #ffffff;
    --accent: #c8102e;
    --faint: #262626;
    --shadow: rgba(0, 0, 0, 0.35);
  }
  html, body {
    margin: 0;
    padding: 0;
    width: 1200px;
    height: 1168px;
    overflow: hidden;
    background: var(--stage);
  }
  .stage {
    position: relative;
    width: 1200px;
    height: 1168px;
  }
  .card {
    position: absolute;
    left: 228px;
    width: 752px;
    height: 468px;
    background: var(--card);
    box-shadow: 4px 6px 10px var(--shadow);
    overflow: hidden;
    color: var(--ink);
    font-family: "Source Sans 3", sans-serif;
    font-weight: 400;
  }
  .card--back { top: 58px; }
  .card--front { top: 614px; }

  .name-watermark {
    position: absolute;
    left: 104px;
    top: 10px;
    margin: 0;
    font-size: 300px;
    line-height: 1;
    letter-spacing: -6px;
    color: var(--faint);
    white-space: nowrap;
  }
  .services {
    position: absolute;
    left: 58px;
    top: 304px;
    width: 680px;
    margin: 0;
    font-size: 20px;
    line-height: 36px;
    white-space: nowrap;
  }
  .services .sep { color: var(--accent); padding: 0 3px; }

  .brand {
    position: absolute;
    left: 58px;
    top: 48px;
    display: flex;
    align-items: center;
    gap: 12px;
    color: var(--ink);
  }
  .brand__name {
    font-size: 118px;
    line-height: 1;
    letter-spacing: -2px;
  }
  .brand__square {
    width: 14px;
    height: 14px;
    background: var(--accent);
    align-self: flex-end;
    margin-bottom: 22px;
  }
  .brand__tagline {
    font-size: 28px;
    line-height: 31px;
    text-transform: uppercase;
  }
  .contact-name {
    position: absolute;
    left: 58px;
    top: 318px;
    margin: 0;
    font-size: 30px;
    line-height: 36px;
    text-transform: uppercase;
  }
  .contact-details {
    position: absolute;
    right: 18px;
    top: 320px;
    margin: 0;
    text-align: right;
    font-size: 20px;
    line-height: 24px;
    font-style: normal;
  }
  .contact-details .phone { font-size: 22px; display: block; margin-bottom: 14px; }
</style>
</head>
<body>
<main class="stage">
  <section class="card card--back" aria-label="Card back: services">
    <p class="name-watermark" aria-hidden="true">K&amp;T</p>
    <p class="services">
      General household repairs and maintenance<span class="sep">|</span>Painting<span class="sep">|</span>Verolin/Plaster<br>
      Repairs<span class="sep">|</span>Fencing<span class="sep">|</span>Gardening and landscaping<span class="sep">|</span>Cleaning and removals<span class="sep">|</span><br>
      Doors and windows<span class="sep">|</span>Hinges and Locks<span class="sep">|</span>Fly screen/ screen door Repairs
    </p>
  </section>

  <section class="card card--front" aria-label="Card front: contact">
    <div class="brand">
      <span class="brand__name">K&amp;T</span>
      <span class="brand__square" aria-hidden="true"></span>
      <span class="brand__tagline">Home<br>Maintenance<br>Services</span>
    </div>
    <p class="contact-name">Lewis Vintelli</p>
    <address class="contact-details">
      <span class="phone">0467205184</span>
      kntmaintenance@postvale.com<br>
      ABN:57140328619
    </address>
  </section>
</main>
</body>
</html>
```